Poster for Network Documentary

I am doing a documentary about the history of America and how it has caused the events that led to the Social Justice Movement in 2020. Need a cover that illustrates that. The title HORIZON 4.1 - "The Crowd Endures". I will need to hand off the editable .psd design to a 3-D animator to create a 5sec bump. Let me know if you need additional direction.

Target Market(s)

Streamvale, KTR, WZB documentaries, ROAM

Industry/Entity Type

Film Production

Font styles to use
Sans Serif

Requirements
Must have
• Bold, Broadcast Network, captivating look
Nice to have
• Bold dynamic text. Should clearly communicate that it's a powerful documentary about the bad history of the USA and the social justice movement of 2020.

```html
<!DOCTYPE html>
<html lang="en">
<head>
<meta charset="utf-8">
<title>HORIZON 4.1 – The Crowd Endures</title>
<link rel="stylesheet" href="https://fonts.googleapis.com/css2?family=Montserrat:wght@400;500;700;800;900&family=Oswald:wght@700&family=Mrs+Saint+Delafield&display=swap">
<style>
  :root {
    --ink: #0e0e0e;
    --shadow: #1c1c1c;
    --hood: #2a2a2a;
    --haze: #e2e2e2;
    --gold: #d9b24a;
    --white: #f2f2f2;
    --grey-text: #bdbdbd;
    --print: #a9a9a9;
  }
  html, body {
    margin: 0;
    padding: 0;
    width: 868px;
    height: 1200px;
    overflow: hidden;
    background: var(--ink);
  }
  .poster {
    position: relative;
    width: 868px;
    height: 1200px;
    overflow: hidden;
    font-family: "Montserrat", Arial, sans-serif;
    color: var(--white);
  }
  .poster__photo {
    position: absolute;
    inset: 0;
    background:
      radial-gradient(ellipse 300px 360px at 868px 250px, var(--haze) 0%, rgba(170,170,170,0.7) 35%, rgba(60,60,60,0) 75%),
      radial-gradient(ellipse 260px 520px at 840px 560px, rgba(120,120,120,0.55) 0%, rgba(40,40,40,0) 80%),
      radial-gradient(ellipse 360px 260px at 420px 560px, rgba(80,80,80,0.8) 0%, rgba(40,40,40,0) 85%),
      radial-gradient(ellipse 420px 260px at 80px 940px, rgba(130,130,130,0.55) 0%, rgba(30,30,30,0) 80%),
      radial-gradient(ellipse 500px 200px at 430px 980px, rgba(100,100,100,0.45) 0%, rgba(30,30,30,0) 80%),
      linear-gradient(90deg, #141414 0%, var(--hood) 30%, #333 60%, #3c3c3c 100%);
  }
  .poster__vignette {
    position: absolute;
    inset: 0;
    background:
      linear-gradient(180deg, rgba(0,0,0,0.35) 0%, rgba(0,0,0,0) 20%, rgba(0,0,0,0) 72%, rgba(0,0,0,0.7) 100%),
      linear-gradient(90deg, rgba(0,0,0,0.45) 0%, rgba(0,0,0,0) 25%);
  }
  .slogan-print {
    position: absolute;
    left: 0;
    width: 100%;
    margin: 0;
    text-align: center;
    font-family: "Montserrat", Arial, sans-serif;
    font-weight: 800;
    line-height: 1;
    color: var(--print);
  }
  .slogan-print--first {
    top: 500px;
    padding-left: 40px;
    box-sizing: border-box;
    font-size: 142px;
    letter-spacing: 2px;
    opacity: 0.78;
  }
  .slogan-print--second {
    top: 720px;
    padding-left: 40px;
    box-sizing: border-box;
    font-size: 120px;
    opacity: 0.14;
  }
  .slogan-print--third {
    top: 1000px;
    padding-left: 40px;
    box-sizing: border-box;
    font-size: 120px;
    opacity: 0.08;
  }
  .kicker {
    position: absolute;
    top: 50px;
    left: 0;
    width: 100%;
    margin: 0;
    text-align: center;
    font-size: 16px;
    font-weight: 500;
    letter-spacing: 9px;
    color: var(--grey-text);
  }
  .release-date {
    position: absolute;
    top: 161px;
    left: 704px;
    width: 80px;
    margin: 0;
    text-align: center;
    font-weight: 700;
    font-size: 33px;
    line-height: 52px;
    color: var(--gold);
  }
  .release-date span { display: block; }
  .title {
    position: absolute;
    top: 800px;
    left: 0;
    width: 100%;
    margin: 0;
    text-align: center;
    font-family: "Oswald", "Arial Narrow", sans-serif;
    font-weight: 700;
    font-size: 110px;
    line-height: 1;
    letter-spacing: 6px;
    color: var(--gold);
    text-shadow: 0 4px 10px rgba(0,0,0,0.75);
  }
  .subtitle {
    position: absolute;
    top: 918px;
    left: 0;
    width: 100%;
    margin: 0;
    text-align: center;
    font-family: "Mrs Saint Delafield", "Brush Script MT", cursive;
    font-weight: 400;
    font-size: 92px;
    line-height: 1;
    color: var(--white);
    text-shadow: 0 2px 6px rgba(0,0,0,0.7);
  }
  .availability {
    position: absolute;
    top: 1058px;
    left: 0;
    width: 100%;
    text-align: center;
  }
  .availability__label {
    margin: 0;
    font-size: 31px;
    font-weight: 800;
    letter-spacing: 1px;
    color: var(--gold);
  }
  .availability__networks {
    margin: 14px 0 0;
    font-size: 16px;
    font-weight: 500;
    color: var(--white);
  }
  .site-url {
    position: absolute;
    top: 1158px;
    left: 0;
    width: 100%;
    margin: 0;
    text-align: center;
    font-size: 14px;
    font-weight: 500;
    letter-spacing: 4px;
    color: var(--grey-text);
  }
</style>
</head>
<body>
  <main class="poster">
    <div class="poster__photo" role="img" aria-label="Black and white photo of a person in a dark hoodie seen from behind, an American flag and smoke below"></div>

    <p class="slogan-print slogan-print--first">BLACK</p>
    <p class="slogan-print slogan-print--second">LIVES</p>
    <p class="slogan-print slogan-print--third">MATTER</p>

    <div class="poster__vignette"></div>

    <p class="kicker">SOCIAL JUSTICE MOVEMENT</p>

    <p class="release-date"><span>29</span><span>05</span><span>21</span></p>

    <h1 class="title">HORIZON 4.1</h1>
    <p class="subtitle">"The Crowd Endures"</p>

    <section class="availability">
      <p class="availability__label">AVAILABLE ON</p>
      <p class="availability__networks">Streamvale, KTR, WZB documentaries, ROAM</p>
    </section>

    <p class="site-url">WWW.YOURSITENAME.COM</p>
  </main>
</body>
</html>
```